Urgent Care opening in Wauchula Florida

we need postcards for our Urgent care that we are opening in Wauchula Florida. We are going to send these postcards in the backpacks for children when the get back to school. I am attaching an idea we foundAddress: 482 N elm lane Wauchula Florida 33873phone # 863-773-4700Hours of business M-F 9-5Saturday 9-5Hours may still changeAlso this design will be used for the banner

Target Market(s)

rural community

Industry/Entity Type

Medical

Other font styles liked:
• any suggested by designer

Requirements
Must have
• see attached file for type of services needed
Nice to have
• see attached file need to have map where office is, services of urgent care

```html
<!DOCTYPE html>
<html lang="en">
<head>
<meta charset="utf-8">
<title>Primeway Care – Opening Postcard</title>
<link rel="stylesheet" href="https://fonts.googleapis.com/css2?family=Open+Sans:wght@400;600;700&family=Roboto+Condensed:wght@400;700&display=swap">
<style>
:root{
  --stage:#2e2e2e;
  --card:#ffffff;
  --blue:#2a4f9e;
  --blue-dark:#1d3a78;
  --green:#3aa142;
  --green-light:#6cc04a;
  --grey:#dcdde0;
  --grey-mid:#b8bac0;
  --ink:#333;
  --red:#d0262c;
}
*{margin:0;padding:0;box-sizing:border-box}
html,body{width:900px;height:1200px;overflow:hidden;background:var(--stage);font-family:"Open Sans",sans-serif;color:var(--ink)}
.card{position:absolute;left:30px;width:840px;height:560px;background:var(--card);overflow:hidden;box-shadow:0 6px 18px rgba(0,0,0,.5)}
.front{top:30px}
.back{top:620px}
.swoosh{position:absolute;inset:0}
.brand{position:absolute;left:400px;top:22px;display:flex;align-items:center;gap:12px}
.brand-mark{width:58px;height:58px;border-radius:50%;background:var(--green)}
.brand-name{font-family:"Roboto Condensed",sans-serif;font-weight:700;font-size:34px;color:var(--green);letter-spacing:1px}
.brand-tag{position:absolute;left:470px;top:70px;font-size:13px;font-style:italic;color:var(--blue)}
.opening{position:absolute;left:0;top:110px;width:370px;height:96px;background:var(--blue);color:#fff;padding:10px 0 0 28px;font-size:31px;line-height:38px;font-weight:600}
.hours{position:absolute;left:0;top:226px;width:330px;height:54px;background:var(--blue-dark);color:#fff;font-weight:700;font-size:36px;padding-left:28px;line-height:54px}
.days{position:absolute;left:28px;top:288px;font-weight:700;font-size:30px;color:var(--blue);white-space:nowrap}
.perks{position:absolute;left:28px;top:340px;list-style:none;width:290px}
.perks li{position:relative;padding-left:22px;font-size:14px;line-height:17px;margin-bottom:7px}
.perks li::before{content:"";position:absolute;left:2px;top:2px;width:6px;height:11px;border:solid var(--red);border-width:0 3px 3px 0;transform:rotate(40deg)}
.photo{position:absolute;left:340px;top:110px;width:500px;height:350px;background:linear-gradient(135deg,#e8eef5 0%,#b9c9dc 55%,#3f62a6 100%)}
.address{position:absolute;left:350px;top:400px;width:210px;height:110px;background:var(--blue);color:#fff;font-family:"Roboto Condensed",sans-serif;font-style:normal;text-transform:uppercase;font-size:21px;line-height:26px;padding:14px 16px}
.back-top{position:absolute;left:0;top:0;width:840px;height:410px;background:linear-gradient(180deg,#eef0f2,var(--grey))}
.col{position:absolute;top:22px;width:360px}
.col-en{left:40px}
.col-es{left:440px}
.col-head{background:var(--green);color:#fff;font-family:"Roboto Condensed",sans-serif;text-transform:uppercase;font-size:22px;line-height:24px;padding:8px 16px;margin-bottom:12px}
.col-es .col-head{text-align:center}
.svc{list-style:none;padding-left:8px}
.svc li{position:relative;padding-left:26px;font-size:16px;line-height:22px;margin-bottom:1px}
.svc li::before{content:"";position:absolute;left:0;top:4px;width:14px;height:14px;border:2px solid var(--grey-mid);background:#fff}
.col-es .svc li{font-size:14px}
.phone{position:absolute;left:40px;top:460px;width:300px;height:54px;border-radius:27px;background:var(--green);display:flex;align-items:center;padding-left:8px;gap:14px;color:#fff;font-weight:700;font-size:26px}
.phone-icon{width:40px;height:40px;border-radius:50%;background:#fff;display:flex;align-items:center;justify-content:center}
.map{position:absolute;left:560px;top:430px;width:240px;height:110px;background:linear-gradient(135deg,#f3f3f3,#d6d8dc);border:2px solid var(--grey-mid)}
</style>
</head>
<body>

<section class="card front">
  <svg class="swoosh" width="840" height="560" viewBox="0 0 840 560" aria-hidden="true">
    <path d="M0 0H840V100C600 80 300 120 0 90Z" fill="#eceef1"/>
    <path d="M0 470C250 420 500 520 840 440V560H0Z" fill="#e3e5e9"/>
    <path d="M300 560C450 500 650 500 840 470V500C650 530 480 540 360 560Z" fill="var(--green)"/>
    <path d="M420 560C560 525 700 520 840 505V560Z" fill="var(--green-light)"/>
  </svg>
  <div class="brand"><span class="brand-mark"></span><span class="brand-name">PRIMEWAY CARE</span></div>
  <p class="brand-tag">Atención médica de urgencia</p>
  <div class="photo" role="img" aria-label="Photo of a doctor team with a nurse and patient in a clinic"></div>
  <h1 class="opening">We are opening in<br>Wauchula Florida</h1>
  <p class="hours">9:00am - 5:00pm</p>
  <p class="days">Monday to Saturday</p>
  <ul class="perks">
    <li>Walk-ins Welcome</li>
    <li>Most Health Insurance and Medicare Welcome</li>
    <li>Usually Lower Co-Payment than an ER</li>
    <li>Accept Cash, Checks, and Credit Cards</li>
  </ul>
  <address class="address">482 N elm lane<br>Wauchula Florida 33873</address>
</section>

<section class="card back">
  <div class="back-top"></div>
  <div class="col col-en">
    <h2 class="col-head">Urgent<br>Medicalcare</h2>
    <ul class="svc">
      <li>General Medical Care</li><li>Colds, Cough and Fever</li><li>Sore Throats</li><li>Influenza</li><li>Ear Infections</li><li>Lacerations and cuts</li><li>Foreign Body Removals</li><li>Burns</li><li>Sprains and Broken Bones</li><li>Minor Surgical Procedures,</li><li>Physical Exams</li><li>Immunizations</li>
    </ul>
  </div>
  <div class="col col-es">
    <h2 class="col-head">Atención médica de<br>urgencia para</h2>
    <ul class="svc">
      <li>General de Atención Médica</li><li>Los resfriados, tos y fiebre</li><li>dolor de garganta</li><li>Influenza</li><li>Infecciones del Oído</li><li>Las laceraciones y cortes</li><li>Mudanzas cuerpo extraño</li><li>Quemaduras</li><li>Esguinces y fracturas de huesos</li><li>Procedimientos quirúrgicos menores,</li><li>Exámenes físicos</li><li>Inmunizaciones</li>
    </ul>
  </div>
  <div class="phone">
    <span class="phone-icon"><svg width="22" height="22" viewBox="0 0 24 24" aria-hidden="true"><path d="M6.6 10.8a15 15 0 0 0 6.6 6.6l2.2-2.2a1 1 0 0 1 1-.25 11.4 11.4 0 0 0 3.6.57 1 1 0 0 1 1 1V20a1 1 0 0 1-1 1A17 17 0 0 1 3 4a1 1 0 0 1 1-1h3.5a1 1 0 0 1 1 1c0 1.25.2 2.45.57 3.6a1 1 0 0 1-.25 1z" fill="var(--green)"/></svg></span>
    841-362-5097
  </div>
  <div class="map" role="img" aria-label="Street map showing the clinic location"></div>
</section>

</body>
</html>
```